I am writing a book called "JOY FINDS THE WAY "

I NEED A BOOK COVER FOR MY BOOK" JOY FINDS THE WAY"
so what was the question? " ( this in smaller font)

"Joy Finds the Way " will need to designed to eventually be a logo , banner and business card
COLOURS MAINLY ORANGE AND WHITE (with accents bright colour )

THE BOOK IS MY JOY JOURNEY AS A PERFORMER AND ADVENTURE INDIA LEARNING ABOUT JOY YOGA WHICH I WILL BE TEACHING

I do not want photos on the front cover ..
The look could be modern and eye-catching
I have also just been to India to learn Laughing Yoga with Dr Rohit Venkatesh

Thank-you so much everyone for your brilliant designs . i am overwhelmed with your talent . i hope to work with you all again soon ! Moira  

Target Market(s)

"Adults based in western speaking countries aged 25 to 60 that want to learn to laugh more
Also this book will be sold at my conference workshops

Industry/Entity Type

Business

Requirements
Must have
• ORANGE AND WHITE
CAN HAVE AQUA , HOT PINK , LIME GREEN, YELLOW ACCENTS

THESE WILL BE DIFFERENT AREAS WILL COVERING IN MY BOOK
EG JOY NAD BREAT CANCER ( PINK)
JOY NAD DEPRESSION ( BLUE)
JOY AND KIDS ( YELLOW)

NO Photos on front cover
Should not have
• No photos

```html
<!DOCTYPE html>
<html lang="en">
<head>
<meta charset="utf-8">
<title>Joy Finds the Way — Book Cover</title>
<link href="https://fonts.googleapis.com/css2?family=Cinzel:wght@400;700&family=EB+Garamond:ital,wght@0,400;1,400&display=swap" rel="stylesheet">
<style>
  :root {
    --backdrop: #383431;
    --cover-orange: #e57818;
    --title-orange: #dd6618;
    --paper: #ffffff;
    --ink: #3a3532;
  }
  html, body {
    margin: 0;
    padding: 0;
    width: 1200px;
    height: 1000px;
    overflow: hidden;
    background: var(--backdrop);
  }
  .canvas {
    position: relative;
    width: 1200px;
    height: 1000px;
  }
  .cover {
    position: absolute;
    left: 241px;
    top: 35px;
    width: 717px;
    height: 927px;
    background: var(--paper);
  }
  .cover__band {
    position: absolute;
    left: 0;
    top: 0;
    width: 100%;
    height: 715px;
    background: var(--cover-orange);
  }
  .cover__word {
    position: absolute;
    left: 0;
    top: 0;
    overflow: visible;
    pointer-events: none;
  }
  .cover__word text {
    font-family: "Cinzel", serif;
    font-weight: 400;
    font-size: 128px;
    fill: var(--title-orange);
  }
  .cover__title {
    position: absolute;
    left: 525px;
    top: 677px;
    margin: 0;
    font-family: "Cinzel", serif;
    font-weight: 700;
    font-size: 19px;
    letter-spacing: 0.2px;
    color: var(--paper);
    white-space: nowrap;
  }
  .cover__author {
    position: absolute;
    left: 739px;
    top: 914px;
    margin: 0;
    font-family: "EB Garamond", serif;
    font-size: 18px;
    color: var(--ink);
    white-space: nowrap;
  }
  .cover__author em {
    font-style: italic;
    margin-right: 4px;
  }
</style>
</head>
<body>
  <main class="canvas">
    <section class="cover" aria-label="Book cover">
      <div class="cover__band"></div>
    </section>
    <svg class="cover__word" width="1200" height="1000" viewBox="0 0 1200 1000" aria-hidden="true">
      <text x="252" y="719" textLength="690" lengthAdjust="spacing">JOY</text>
    </svg>
    <h1 class="cover__title">“JOY FINDS THE WAY”</h1>
    <p class="cover__author"><em>by</em> Moira Pendry</p>
  </main>
</body>
</html>
```